smile partners of lakeview | ||
business cards/stationary | ||
Cutting-Edge Professional |
Dr. Marcus Holloway / Dr. Leonardo Brisco | ||
President | ||
Bayonne 57 Ave K Harborview, NJ 07110 201-555-0142 ********* East Orange 42 North Whitfield St Suite 208 Westbrook, NJ 07120 973-555-0187 ******** North Bergen 4829 Larkmoor Pinecrest, NJ 07140 201-555-0163 ********** Union City 2748 Quenton Ave Millbrook, NJ 07130 201-555-0129 ********* Paterson 3170 Elm street Suite K Cedar Falls, NJ 07150 973 555-0114 ******** |
office@quentondental.example | ||
www.SmilePartnersOfLV.example | ||
We need 7 different business card designs. 1. Dr Marcus Holloway (no address..just website) 2. Dr Leonardo Brisco (no address just website) 3. Smile Partners of Lakeview - East Orange 4. Smile Partners of Lakeview - Bayone 5. Smile Partners of Lakeview- Union City 6. Smile Partners of Lakeview- North Bergen 7. Smile Partners of Lakeview- Paterson Business Cards 3-7 do not need to include Dr Holloway/Dr Brisco's name on them |
For the personal cards (Dr Marcus Holloway and Dr Leo Brisco) use the back of the cards to tell all of the office locations For the Office cards (3-7) use the back of the card for appointments...we will upload a sample background that we currently use. |
554611_1195_4351.png |
photo3_JPG4352.jpg |
DentalGroups_Paterson_4421.pdf |
DentalGroups_Paterson_4422.gif |
DentalGroups_Paterson_4423.eps |
DentalGroups_Web_4424.png |
DentalGroups_Web_4425.ai |
DentalGroups_Web_4426.gif |

```html
<!DOCTYPE html>
<html lang="en">
<head>
<meta charset="utf-8">
<title>Smile Partners of Lakeview — Business Card</title>
<link href="https://fonts.googleapis.com/css2?family=Source+Sans+3:wght@400;600&family=Libre+Baskerville&display=swap" rel="stylesheet">
<style>
  :root {
    --page: #f1eee9;
    --card-white: #ffffff;
    --brand-brown: #7a3f0c;
    --brown-light: #b36a1f;
    --brown-mid: #8a4710;
    --brown-dark: #4e2304;
    --divider-green: #d7e6cf;
    --text-light: #fbf3e6;
  }
  html, body {
    margin: 0;
    padding: 0;
    width: 1200px;
    height: 802px;
    overflow: hidden;
    background: var(--page);
  }
  .canvas {
    position: relative;
    width: 1200px;
    height: 802px;
    overflow: hidden;
  }

  /* Front of card */
  .card-front {
    position: absolute;
    left: 259px;
    top: 0;
    width: 682px;
    height: 384px;
    display: flex;
  }
  .front-brand {
    width: 442px;
    background: var(--card-white);
    position: relative;
  }
  .front-divider {
    width: 12px;
    background: var(--divider-green);
  }
  .front-person {
    flex: 1;
    position: relative;
    background: radial-gradient(ellipse 90% 60% at 50% 38%, var(--brown-light) 0%, var(--brown-mid) 45%, var(--brown-dark) 100%);
    color: var(--text-light);
    font-family: "Source Sans 3", sans-serif;
  }
  .brand-name {
    position: absolute;
    left: 0;
    right: 0;
    top: 168px;
    text-align: center;
    font-family: "Source Sans 3", sans-serif;
    font-weight: 600;
    color: var(--brand-brown);
    font-size: 34px;
    line-height: 38px;
    margin: 0;
  }
  .brand-web {
    position: absolute;
    left: 0;
    right: 0;
    top: 252px;
    text-align: center;
    font-family: "Source Sans 3", sans-serif;
    font-weight: 600;
    font-size: 9px;
    letter-spacing: 0.5px;
    color: var(--brand-brown);
    margin: 0;
  }
  .person-name {
    position: absolute;
    left: 0;
    right: 0;
    top: 168px;
    text-align: center;
    font-size: 21px;
    margin: 0;
    font-weight: 400;
  }
  .person-title {
    position: absolute;
    left: 0;
    right: 0;
    top: 198px;
    text-align: center;
    font-size: 8px;
    letter-spacing: 1px;
    margin: 0;
  }
  .person-email {
    position: absolute;
    left: 30px;
    top: 352px;
    font-size: 10px;
    margin: 0;
  }

  /* Back of card */
  .card-back {
    position: absolute;
    left: 259px;
    top: 408px;
    width: 682px;
    height: 394px;
    background: radial-gradient(ellipse 70% 55% at 50% 30%, var(--brown-light) 0%, var(--brown-mid) 45%, var(--brown-dark) 100%);
    color: var(--text-light);
  }
  .back-brand {
    position: absolute;
    left: 0;
    right: 0;
    top: 48px;
    text-align: center;
    font-family: "Source Sans 3", sans-serif;
    font-weight: 600;
    font-size: 19px;
    line-height: 21px;
    margin: 0;
  }
  .office {
    position: absolute;
    font-family: "Libre Baskerville", serif;
    font-size: 9.5px;
    line-height: 12.5px;
    margin: 0;
    font-style: normal;
    white-space: nowrap;
  }
  .office-harborview { left: 89px; top: 152px; }
  .office-westbrook { left: 250px; top: 152px; }
  .office-millbrook { left: 439px; top: 152px; }
  .office-pinecrest { left: 161px; top: 260px; }
  .office-cedar-falls { left: 360px; top: 260px; }
</style>
</head>
<body>
<main class="canvas">
  <section class="card-front" aria-label="Card front">
    <div class="front-brand">
      <h1 class="brand-name">Smile Partners<br>of Lakeview</h1>
      <p class="brand-web">www.SmilePartnersOfLV.example</p>
    </div>
    <div class="front-divider"></div>
    <div class="front-person">
      <p class="person-name">Dr. Marcus Holloway</p>
      <p class="person-title">PRESIDENT</p>
      <p class="person-email">Email : dr.marcusholloway@mail.example</p>
    </div>
  </section>

  <section class="card-back" aria-label="Card back with office locations">
    <h2 class="back-brand">Smile Partners<br>of Lakeview</h2>

    <address class="office office-harborview">Harborview Family Dental<br>57 Ave K<br>Harborview, NJ 07110<br>(201) 555-0142<br>(201) 555-0150 (FAX)</address>

    <address class="office office-westbrook">Westbrook Family Dental<br>42 North Whitfield St<br>Suite 208<br>Westbrook, NJ 07120<br>(973) 555-0187<br>(973) &nbsp;&nbsp;&nbsp;&nbsp;&nbsp;&nbsp;&nbsp;&nbsp;&nbsp;&nbsp;(FAX)</address>

    <address class="office office-millbrook">Millbrook Family Dental<br>2748 Quenton Ave<br>Millbrook, NJ 07130<br>(201) 555-0129<br>(201) &nbsp;&nbsp;&nbsp;&nbsp;&nbsp;&nbsp;&nbsp;&nbsp;&nbsp;&nbsp;(FAX)</address>

    <address class="office office-pinecrest">Pinecrest Family Dental<br>4829 Larkmoor<br>Pinecrest, NJ 07140<br>(201) 555-0163<br>(201) &nbsp;&nbsp;&nbsp;&nbsp;&nbsp;&nbsp;&nbsp;&nbsp;&nbsp;&nbsp;(FAX)</address>

    <address class="office office-cedar-falls">Cedar Falls Family Dental<br>3170 Elm street<br>Suite K<br>Cedar Falls, NJ 07150<br>(973) 555-0114<br>(973) &nbsp;&nbsp;&nbsp;&nbsp;&nbsp;&nbsp;&nbsp;&nbsp;&nbsp;&nbsp;(FAX)</address>
  </section>
</main>
</body>
</html>
```